Lorna Tess Tresses Fancy Business Card’s

I want my business cards to be elite, original and very classy. I want the business cards to match the colors of my logo and to match the design posted. I would love the design of the picture I posted

I want the card all white .
The dripping on the top of the card I want it to match the pink color in my logo that’s also posted .
I need my logo on the business card !
I need my Instagram- @lorna.tess.tresses__
And my phone number - 582 907 3365

Target Market(s)

My target market is young woman age 23 to older woman to the age of 65
I want both older and younger women to love my design . I don’t want any cheap looking business cards

Industry/Entity Type

Hair And Beauty

Contact Information for Business Card

Add my logo
Add my Instagram- @lorna.tess.tresses__
My number - 582 907 3365
My website- www.lornatesstresses.example

Font styles to use
Serif
Script

Colors
ffffff
e667a6
e34298

Requirements
Must have
• The business cards must have my logo, my number , my website, and my Instagram!
Nice to have
• Nice to have glitter words that match my logo
• The business cards must look classy and mature
• I want them to be very unique!!
Should not have
• Should not have any colors that doesn’t match my logo ! This is very important! Please

```html
<!DOCTYPE html>
<html lang="en">
<head>
<meta charset="utf-8">
<title>Lorna Tess Tresses – Business Cards</title>
<link rel="stylesheet" href="https://fonts.googleapis.com/css2?family=Cinzel:wght@500&family=Playfair+Display:wght@600&family=Poppins:wght@400&display=swap">
<style>
  :root {
    --backdrop: #d9d9db;
    --card: #ffffff;
    --pink: #e34298;
    --pink-soft: #e667a6;
    --white: #ffffff;
  }
  * { box-sizing: border-box; margin: 0; padding: 0; }
  html, body { width: 1200px; height: 800px; overflow: hidden; }
  body {
    background: var(--backdrop);
    position: relative;
    font-family: "Poppins", sans-serif;
  }
  .card {
    position: absolute;
    top: 245px;
    width: 540px;
    height: 310px;
    background: var(--card);
    border-bottom: 4px solid var(--pink);
    box-shadow: 0 10px 24px rgba(0,0,0,0.18);
    overflow: hidden;
  }
  .card--info { left: 40px; }
  .card--brand { left: 620px; }

  .drip {
    position: absolute;
    left: 0;
    right: 0;
    top: 0;
    height: 34px;
    background: linear-gradient(var(--pink), var(--pink-soft));
  }

  .brand-name {
    font-family: "Playfair Display", serif;
    font-weight: 600;
    color: var(--pink);
    white-space: nowrap;
  }

  /* info side */
  .card--info .brand-name {
    position: absolute;
    right: 34px;
    top: 58px;
    font-size: 22px;
  }
  .divider {
    position: absolute;
    left: 28px;
    right: 28px;
    top: 182px;
    height: 1px;
    background: var(--pink-soft);
  }
  .holder {
    position: absolute;
    left: 34px;
    top: 130px;
  }
  .holder__name {
    font-family: "Cinzel", serif;
    font-weight: 500;
    font-size: 20px;
    color: var(--pink);
    letter-spacing: 0.5px;
    line-height: 1.1;
  }
  .holder__role {
    font-size: 12px;
    color: var(--pink-soft);
    margin-top: 4px;
  }
  .contacts {
    position: absolute;
    top: 198px;
    list-style: none;
    font-size: 12.5px;
    color: var(--pink);
  }
  .contacts--left { left: 34px; }
  .contacts--right { right: 34px; text-align: right; }
  .contacts li {
    display: flex;
    align-items: center;
    gap: 8px;
    height: 22px;
    white-space: nowrap;
  }
  .contacts--right li { justify-content: flex-end; }
  .contact-icon {
    width: 14px;
    height: 14px;
    flex: none;
  }

  /* brand side */
  .card--brand .brand-name {
    position: absolute;
    left: 0;
    right: 0;
    top: 50%;
    transform: translateY(-50%);
    text-align: center;
    font-size: 38px;
  }
</style>
</head>
<body>

<section class="card card--info" aria-label="Business card, contact side">
  <div class="drip" role="img" aria-label="Pink paint drip decoration along the top edge"></div>

  <p class="brand-name">Lorna Tess Tresses</p>

  <div class="holder">
    <p class="holder__name">Dana Whitfield</p>
    <p class="holder__role">President</p>
  </div>

  <div class="divider"></div>

  <ul class="contacts contacts--left">
    <li>
      <svg class="contact-icon" viewBox="0 0 14 14" aria-hidden="true">
        <rect width="14" height="14" rx="3" fill="var(--pink-soft)"/>
        <path d="M4.3 3.2 L5.6 3.2 L6.2 5 L5.3 5.7 Q6 7.5 8.3 8.7 L9 7.8 L10.8 8.4 L10.8 9.7 Q10.5 10.8 9.3 10.8 Q3.2 10.2 3.2 4.4 Q3.3 3.3 4.3 3.2 Z" fill="var(--white)"/>
      </svg>
      582 907 3365
    </li>
    <li>
      <svg class="contact-icon" viewBox="0 0 14 14" aria-hidden="true">
        <rect width="14" height="14" rx="3" fill="var(--pink-soft)"/>
      </svg>
      @lorna.tess.tresses__
    </li>
  </ul>

  <ul class="contacts contacts--right">
    <li>
      info@lornatesstresses.example
      <svg class="contact-icon" viewBox="0 0 14 14" aria-hidden="true">
        <rect width="14" height="14" rx="3" fill="var(--pink-soft)"/>
        <rect x="3" y="4.2" width="8" height="5.6" fill="none" stroke="var(--white)" stroke-width="1.1"/>
        <path d="M3 4.4 L7 7.4 L11 4.4" fill="none" stroke="var(--white)" stroke-width="1.1"/>
      </svg>
    </li>
    <li>
      www.lornatesstresses.example
      <svg class="contact-icon" viewBox="0 0 14 14" aria-hidden="true">
        <rect width="14" height="14" rx="3" fill="var(--pink-soft)"/>
        <circle cx="7" cy="7" r="3.8" fill="none" stroke="var(--white)" stroke-width="1.1"/>
        <path d="M3.2 7 H10.8 M7 3.2 Q5 7 7 10.8 M7 3.2 Q9 7 7 10.8" fill="none" stroke="var(--white)" stroke-width="0.9"/>
      </svg>
    </li>
  </ul>
</section>

<section class="card card--brand" aria-label="Business card, brand side">
  <div class="drip" role="img" aria-label="Pink paint drip decoration along the top edge"></div>
  <p class="brand-name">Lorna Tess Tresses</p>
</section>

</body>
</html>
```